We are wanting a designer to design an ebook on Residential Property in Australia. This ebook is a quarterly report and covers 5 major capital cities in Australia. This is the first quarterly report for the year - another 3 are needed to be created. If you are chosen as our designer please expect ongoing work which is well rewarded.

To begin with:

We will only need you to design a few pages so we can see your style. Then if you are chosen we will get you to do the whole thing.

Can you please design the title page, page 5 and the Adelaide section(page 6 & 7) of the The Housing Market Horizon - Seasonal Capital Review - Q1 2014 document attached.

The ebook brief:

You will need to create 2 graphs to include in the ebook from the data I give to you for each capital city (one graph for houses and one graph for units).

We already have a style of ebook in mind from a previous ebook our in-office designer has created for our company. You will need to keep with the logo/style/colours/fonts etc. We are looking for a designer based in Australia.

Sources and content:

Below I have shared a dropbox folder with you. It contains the first ebook our designer has created for you to view the style,logo etc - CoralPeak-Homes-ebook. The folder also contains the source files for the logo.

https://www.filevaultex.com/sh/4k2pwq7zz8m3rd/BBQ519jtkw04xPLNZRWUVB_qmtc#/

The Housing Market Horizon - Seasonal Capital Review - Q1 2014 document attached is the content we need made into the ebook.

Each page has been set out with the content needed for that page. Each capital city content spreads out over two pages with a graph on each. I have highlighted in red the data needed to create each of the graphs. The graph style must look like the Market Outlook image in the shared dropbox folder.

You will also need to redesign the graph on page 5. You may do this how you like as long as it keeps in the style of the ebook. We will also need the source files on this ebook.

```html
<!DOCTYPE html>
<html lang="en">
<head>
<meta charset="utf-8">
<title>CoralPeak Homes – Residential Property Outlook</title>
<link href="https://fonts.googleapis.com/css2?family=Carlito:wght@400;700&family=Montserrat:wght@600&display=swap" rel="stylesheet">
<style>
  :root {
    --brand-red: #c8242c;
    --ink: #231f20;
    --paper: #ffffff;
    --sky: #5f7391;
    --dusk: #8a8d99;
    --timber: #6b4a34;
    --glow: #c99a5e;
    --pool-light: #4f7fc6;
    --pool-deep: #1f3f8f;
  }
  * { margin: 0; padding: 0; box-sizing: border-box; }
  html, body { width: 848px; height: 1200px; overflow: hidden; background: var(--paper); }
  .cover {
    position: relative;
    width: 848px;
    height: 1200px;
    background: var(--paper);
    font-family: "Carlito", "Calibri", sans-serif;
  }
  .masthead {
    position: absolute;
    top: 0; left: 0;
    width: 848px; height: 211px;
    display: flex;
    align-items: center;
    justify-content: center;
    gap: 22px;
  }
  .masthead-mark {
    width: 56px; height: 56px;
    background: var(--brand-red);
  }
  .masthead-name {
    font-family: "Montserrat", sans-serif;
    font-weight: 600;
    font-size: 54px;
    letter-spacing: 8px;
    color: var(--ink);
    text-transform: uppercase;
  }
  .hero-photo {
    position: absolute;
    top: 211px; left: 0;
    width: 848px; height: 989px;
    background: linear-gradient(180deg,
      var(--dusk) 0%,
      var(--sky) 10%,
      var(--timber) 22%,
      var(--glow) 38%,
      var(--timber) 52%,
      var(--pool-light) 62%,
      var(--pool-deep) 100%);
  }
  .title-panel {
    position: absolute;
    left: 204px; top: 782px;
    width: 620px; height: 220px;
    background: var(--brand-red);
    color: var(--paper);
    padding: 22px 0 0 26px;
  }
  .title-panel h1 {
    font-weight: 400;
    font-size: 58px;
    line-height: 60px;
  }
  .title-panel .subtitle {
    font-size: 32px;
    margin-top: 8px;
    padding-left: 8px;
  }
  .city-tab {
    position: absolute;
    bottom: 0;
    width: 50px;
    background: var(--brand-red);
    color: var(--paper);
    display: flex;
    align-items: center;
    justify-content: center;
  }
  .city-tab span {
    writing-mode: vertical-rl;
    transform: rotate(180deg);
    font-size: 26px;
    line-height: 1;
  }
  .city-adelaide  { left: 482px; top: 1062px; }
  .city-brisbane  { left: 553px; top: 1062px; }
  .city-melbourne { left: 624px; top: 1026px; }
  .city-perth     { left: 695px; top: 1097px; }
  .city-sydney    { left: 767px; top: 1080px; }
</style>
</head>
<body>
  <main class="cover">
    <header class="masthead">
      <div class="masthead-mark"></div>
      <div class="masthead-name">CoralPeak</div>
    </header>

    <div class="hero-photo" role="img" aria-label="Photograph of a luxury timber-framed pavilion home at dusk, glowing windows and two lounge chairs on a deck beside a blue-tiled swimming pool"></div>

    <section class="title-panel">
      <h1>Residential Property<br>Outlook</h1>
      <p class="subtitle">Capital City Market Report</p>
    </section>

    <nav class="city-tabs">
      <div class="city-tab city-adelaide"><span>Adelaide</span></div>
      <div class="city-tab city-brisbane"><span>Brisbane</span></div>
      <div class="city-tab city-melbourne"><span>Melbourne</span></div>
      <div class="city-tab city-perth"><span>Perth</span></div>
      <div class="city-tab city-sydney"><span>Sydney</span></div>
    </nav>
  </main>
</body>
</html>
```